Medical business needs responsive Bootstrap theme design

We need a responsive Twitter Bootstrap theme for a hair transplant business in South Korea which looks good from full size desktop screens down to smartphone displays. We would like the site to match in style with our brochure design (see the PDF and Adobe Illustrator files), although it does not need to match exactly. Please feel free to use the design elements and images in the brochure. The general flow of the theme is shown in the wireframe image.
We expect graphic design, images, CSS, and HTML. No PHP/backend/ecommerce integration is expected.
Here are the links to the 3 stock images in the brochure:
http://www.pixelvantry.com/pic.mhtml?id=918270563
http://www.lumoframes.com/photo/hair-transplant-gm730418256-61920475
http://www.lumoframes.com/photo/doctor-inspecting-skin-of-head-gm842067319-57301846
You can use the Bootstrap template here as a starting point: http://kelvarnlayouts.com/template-overviews/agency/
Target Market(s)
Our primary customers will be Westerners aged 28-45
Industry/Entity Type
Plastic Surgery
Coding
Coded - Design and coding required
Number of Pages Required
1 page

```html
<!DOCTYPE html>
<html lang="en">
<head>
<meta charset="utf-8">
<title>Hanbit Hair Restoration Center</title>
<link href="https://fonts.googleapis.com/css2?family=Quicksand:wght@500;700&family=Open+Sans:ital,wght@0,400;0,600;0,700;1,400&display=swap" rel="stylesheet">
<style>
:root{
  --blue:#2c6db3;
  --blue-dark:#1f528f;
  --blue-head:#2f62a8;
  --blue-light:#dfe9f5;
  --text:#444;
  --muted:#777;
  --grey-bg:#f2f2f2;
  --card-bg:#ececec;
  --line:#dcdcdc;
  --dark:#2b2b2b;
  --star:#e8a21b;
}
*{box-sizing:border-box;margin:0;padding:0}
html,body{width:1200px;height:4369px;overflow:hidden}
body{font-family:"Open Sans",Arial,sans-serif;color:var(--text);background:#fff;position:relative}
.section{position:absolute;left:0;width:1200px}
.abs{position:absolute}
.heading{position:absolute;left:0;width:1200px;text-align:center;font-family:"Quicksand",Arial,sans-serif;font-weight:700;font-size:33px;color:var(--blue-head)}
.divider{position:absolute;left:480px;width:240px;height:20px}
.btn{position:absolute;background:var(--blue);color:#fff;font-size:13px;text-align:center;border-radius:2px}

/* header */
.site-header{top:0;height:131px;border-top:5px solid var(--blue);background:#fff}
.brand{position:absolute;left:100px;top:36px;display:flex;align-items:center;gap:14px}
.brand-dot{width:58px;height:58px;border-radius:50%;background:var(--blue)}
.brand-name{font-family:"Quicksand",Arial,sans-serif;font-weight:700;font-size:26px;color:var(--blue-dark)}
.menu-toggle{position:absolute;left:1070px;top:56px;width:28px}
.menu-toggle span{display:block;height:4px;background:#222;margin-bottom:5px}

/* hero */
.hero{top:131px;height:519px;background:linear-gradient(90deg,#9fb6c8 0%,#d9dde0 40%,#f1f1f0 62%,#f6f6f5 100%)}
.hero-photo{position:absolute;left:0;top:0;width:690px;height:519px;background:linear-gradient(100deg,#6f8fb0 0%,#a8b8c6 35%,#c9b7a5 60%,rgba(240,240,238,0) 100%)}
.hero-mark{position:absolute;left:724px;top:158px;width:60px;height:60px;border-radius:50%;background:var(--blue)}
.hero-title{position:absolute;left:724px;top:240px;font-family:"Quicksand",Arial,sans-serif;font-weight:700;font-size:29px;color:var(--blue)}
.hero-text{position:absolute;left:724px;top:284px;width:380px;font-size:15px;line-height:24px;color:#555}
.hero .btn{left:722px;top:347px;width:146px;height:42px;line-height:42px;font-size:14px}
.hero-arrow{position:absolute;left:1140px;top:230px}

/* why */
.why{top:650px;height:568px;background:#fff}
.feature{position:absolute;top:224px;width:306px;height:285px;background:var(--card-bg);text-align:center;box-shadow:0 2px 4px rgba(0,0,0,.12)}
.feature-icon{position:absolute;left:74px;top:-79px;width:158px;height:158px;border-radius:50%;background:#fff;box-shadow:0 2px 6px rgba(0,0,0,.2)}
.feature-icon .inner{position:absolute;left:12px;top:12px;width:134px;height:134px;border-radius:50%;background:linear-gradient(180deg,#3b7cc4,#22589a);display:flex;align-items:center;justify-content:center}
.feature h3{position:absolute;top:103px;left:0;width:100%;font-size:16px;font-weight:700;color:#222}
.feature p{position:absolute;top:126px;left:22px;width:262px;font-size:12.5px;line-height:18px;color:#555}
.feature .btn{left:104px;top:224px;width:98px;height:34px;line-height:34px}

/* methods */
.methods{top:1218px;height:792px;background:var(--grey-bg)}
.methods .sub{position:absolute;top:114px;left:0;width:1200px;text-align:center;font-style:italic;font-size:14px;color:#888}
.method{position:absolute;top:166px;height:574px;background:#fff;box-shadow:0 1px 3px rgba(0,0,0,.1)}
.method h3{position:absolute;left:22px;top:22px;font-family:"Quicksand",Arial,sans-serif;font-weight:700;font-size:19px;color:var(--blue)}
.method .lead{position:absolute;left:22px;top:52px;font-size:13px;color:#555}
.step{position:absolute;left:22px;height:146px;width:460px}
.step-img{position:absolute;left:0;top:0;width:146px;height:146px;border-radius:50%;border:5px solid #e2e2e2;background:radial-gradient(circle,#c99a80 0%,#8a6450 60%,#5a4236 100%)}
.step-bubble{position:absolute;left:150px;top:22px;width:286px;height:102px;border:1px solid #ddd;border-radius:0 40px 40px 0;padding:12px 16px;font-size:13px;line-height:21px;color:#444;background:#fff}

/* comparison */
.comparison{top:2010px;height:577px;background:#fff}
.compare-table{position:absolute;left:90px;top:143px;width:1005px;border-collapse:collapse;font-size:13px;color:#444;box-shadow:0 1px 3px rgba(0,0,0,.12)}
.compare-table th{height:64px;background:linear-gradient(180deg,#f1f1f1,#d9d9d9);text-align:left;font-weight:600;padding-left:30px;font-size:13px}
.compare-table td{height:53px;padding-left:30px;border-top:1px solid #e3e3e3}
.compare-table tr:nth-child(even) td{background:var(--blue-light)}
.compare-table tr:nth-child(odd) td{background:#f7f7f7}
.compare-table td,.compare-table th{border-right:1px solid #e3e3e3}

/* contact */
.contact{top:2587px;height:524px;background:var(--dark)}
.contact-map{position:absolute;inset:0;background:linear-gradient(135deg,#3a3a3a,#232323 55%,#2f2f2f)}
.contact .heading{color:#fff;top:92px}
.contact-input{position:absolute;left:347px;top:174px;width:355px;height:41px;background:#fff;font-size:13px;color:#888;padding:11px 12px}
.contact .btn{left:714px;top:174px;width:139px;height:41px;line-height:41px;font-size:14px;border-radius:0}
.contact-box{position:absolute;left:347px;top:224px;width:506px;height:210px;background:var(--blue)}
.contact-brand{position:absolute;left:26px;top:98px;display:flex;align-items:center;gap:10px;color:#fff;font-family:"Quicksand",Arial,sans-serif;font-weight:700;font-size:16px}
.contact-brand .dot{width:40px;height:40px;border-radius:50%;background:#fff}
.contact-line{position:absolute;left:286px;color:#fff;font-size:14px;display:flex;align-items:center;gap:10px}
.social{position:absolute;display:flex;gap:8px}
.social span{width:28px;height:28px;border-radius:50%;background:#e84b3c}
.social span:nth-child(1){background:#3b5998}
.social span:nth-child(2){background:#2aa3ef}
.social span:nth-child(4){background:#0e76a8}

/* testimonials */
.testimonials{top:3111px;height:618px;background:#fff}
.testimonial{position:absolute;top:152px;width:312px;height:416px;background:#fff;border:1px solid #ddd;text-align:center}
.testimonial-photo{position:absolute;left:0;top:0;width:310px;height:209px;display:flex}
.testimonial-photo .half{flex:1;position:relative;background:linear-gradient(180deg,#d8d8d8,#8d8d8d)}
.testimonial-photo .half span{position:absolute;bottom:6px;font-size:13px;font-weight:600;color:#fff}
.testimonial-photo .half:first-child span{left:14px}
.testimonial-photo .half:last-child span{right:14px}
.testimonial h4{position:absolute;top:235px;width:100%;font-size:20px;font-weight:600;color:#222}
.stars{position:absolute;top:264px;width:100%;color:var(--star);font-size:13px;letter-spacing:1px}
.testimonial p{position:absolute;top:290px;left:26px;width:258px;font-size:13px;line-height:20px;color:#444}

/* blog */
.blog{top:3729px;height:591px;background:var(--grey-bg)}
.post{position:absolute;top:125px;width:312px;height:405px;background:#fff;box-shadow:0 1px 3px rgba(0,0,0,.1)}
.post-img{position:absolute;left:0;top:0;width:312px;height:201px}
.post h4{position:absolute;left:22px;top:216px;font-size:14.5px;font-weight:700;color:#222}
.post .meta{position:absolute;left:22px;top:246px;font-size:12px;color:#666;display:flex;gap:14px;align-items:center}
.post p{position:absolute;left:22px;top:270px;width:272px;font-size:12.5px;line-height:20px;color:#444}
.post .more{position:absolute;left:22px;top:362px;font-size:13px;color:var(--blue);text-decoration:underline}

/* footer */
.site-footer{top:4320px;height:49px;background:var(--blue)}
.site-footer .copy{position:absolute;left:100px;top:16px;font-size:12px;color:#fff}
.footer-icons{position:absolute;left:928px;top:10px;display:flex;gap:8px}
.footer-icons span{width:28px;height:28px;border-radius:50%;border:1.5px solid #fff}
</style>
</head>
<body>

<header class="section site-header">
  <div class="brand"><div class="brand-dot"></div><div class="brand-name">Hanbit Hair Restoration Center</div></div>
  <div class="menu-toggle"><span></span><span></span><span></span></div>
</header>

<section class="section hero">
  <div class="hero-photo" role="img" aria-label="Surgeon wearing a loupe headset marking the scalp of a bearded male patient"></div>
  <div class="hero-mark"></div>
  <h1 class="hero-title">Hanbit Hair Restoration Center</h1>
  <p class="hero-text">Hair Restoration Surgery has improved significantly over the last decade.</p>
  <a class="btn">View more info</a>
  <svg class="hero-arrow" width="20" height="60" viewBox="0 0 20 60"><path d="M2 2 L18 30 L2 58" fill="none" stroke="#999" stroke-width="2"/></svg>
</section>

<section class="section why">
  <h2 class="heading" style="top:40px">Why South Korea?</h2>
  <svg class="divider" style="top:94px" viewBox="0 0 240 20"><line x1="0" y1="10" x2="105" y2="10" stroke="#555" stroke-width="1.5"/><line x1="135" y1="10" x2="240" y2="10" stroke="#555" stroke-width="1.5"/><circle cx="120" cy="10" r="7" fill="none" stroke="#999" stroke-width="2"/></svg>

  <div class="feature" style="left:96px">
    <div class="feature-icon"><div class="inner"><svg width="60" height="60" viewBox="0 0 60 60" fill="none" stroke="#fff" stroke-width="3"><path d="M30 34 C30 22 38 14 48 14 C48 26 40 34 30 34 Z"/><path d="M30 34 C30 26 24 20 16 20 C16 28 22 34 30 34 Z"/><path d="M8 50 L22 42 L40 46 L54 38"/></svg></div></div>
    <h3>QUALITY OF CARE</h3>
    <p>Hair Restoration Surgery has improved significantly over the last decade. State-of-the-art technology ensures transplanted hair is strategically placed for a natural look.</p>
    <a class="btn">Read More</a>
  </div>
  <div class="feature" style="left:446px">
    <div class="feature-icon"><div class="inner"><svg width="60" height="60" viewBox="0 0 60 60" fill="none" stroke="#fff" stroke-width="3"><circle cx="30" cy="32" r="22"/><path d="M30 18 V32 L40 38"/><path d="M24 6 H36"/></svg></div></div>
    <h3>CONVENIENCE</h3>
    <p>You are already in South Korea or Japan. The procedure can be done in one day with follow-up appointments available on request (though generally not needed).</p>
    <a class="btn">Read More</a>
  </div>
  <div class="feature" style="left:789px">
    <div class="feature-icon"><div class="inner"><svg width="60" height="60" viewBox="0 0 60 60" fill="none" stroke="#fff" stroke-width="3"><path d="M22 10 H38 L34 20 H26 Z"/><path d="M26 20 C12 28 10 52 30 52 C50 52 48 28 34 20"/><path d="M30 28 V46 M36 31 H27 a3 3 0 0 0 0 6 h6 a3 3 0 0 1 0 6 H24"/></svg></div></div>
    <h3>QUALITY OF CARE</h3>
    <p>The average hair transplant surgery in South Korea costs about $5,000 to $6,000 (30-40% less than if done in the United States). The average hair transplant surgery in South Korea</p>
    <a class="btn">Read More</a>
  </div>
</section>

<section class="section methods">
  <h2 class="heading" style="top:42px">Methods</h2>
  <svg class="divider" style="top:88px" viewBox="0 0 240 20"><line x1="0" y1="10" x2="105" y2="10" stroke="#555" stroke-width="1.5"/><line x1="135" y1="10" x2="240" y2="10" stroke="#555" stroke-width="1.5"/><circle cx="120" cy="10" r="7" fill="none" stroke="#999" stroke-width="2"/></svg>
  <p class="sub">There are two hair replacement methods surgeons use depending on a patient's goals.</p>

  <div class="method" style="left:96px;width:501px">
    <h3>FUT (Traditional Follicular Unit Transplant)</h3>
    <p class="lead">Can wear hair short. Leaves faint linear scar.</p>
    <div class="step" style="top:93px"><div class="step-img" role="img" aria-label="Diagram of a strip of scalp removed from the back of the head"></div><div class="step-bubble">Hair on back of head is trimmed and a narrow strip is surgically removed so that hair can grow through and camouflage the scar.</div></div>
    <div class="step" style="top:250px"><div class="step-img" role="img" aria-label="Close-up diagram of the donor strip being sutured"></div><div class="step-bubble">Hair on back of head is trimmed and a narrow strip is surgically removed so that hair can grow through and camouflage the scar.</div></div>
    <div class="step" style="top:404px"><div class="step-img" role="img" aria-label="Close-up of healed scalp with hair growing over the scar"></div><div class="step-bubble">Hair on back of head is trimmed and a narrow strip is surgically removed so that hair can grow through and camouflage the scar.</div></div>
  </div>

  <div class="method" style="left:609px;width:486px">
    <h3>FUE (Follicular Unite Extraction)</h3>
    <p class="lead">Can wear hair buzzed. Leaves diffuse pinpoint scarring.</p>
    <div class="step" style="top:93px"><div class="step-img" role="img" aria-label="Diagram of a punch device extracting follicles"></div><div class="step-bubble">Donor area on back of head is shaved to allow hair to be extracted with a tiny punch device.</div></div>
    <div class="step" style="top:250px"><div class="step-img" role="img" aria-label="Diagram of individual follicles being removed"></div><div class="step-bubble">Hair follicles are individually selected with proper space to avoid any visible thinning or scarring. Then each follicle is gently removed</div></div>
    <div class="step" style="top:404px"><div class="step-img" role="img" aria-label="Diagram of scalp showing tiny punch marks"></div><div class="step-bubble">By using tiny 1-1.0mm punches, the minuscule dots that remain are nearly invisible without magnification</div></div>
  </div>
</section>

<section class="section comparison">
  <h2 class="heading" style="top:56px">Comparison</h2>
  <svg class="divider" style="top:100px" viewBox="0 0 240 20"><line x1="0" y1="10" x2="105" y2="10" stroke="#555" stroke-width="1.5"/><line x1="135" y1="10" x2="240" y2="10" stroke="#555" stroke-width="1.5"/><circle cx="120" cy="10" r="7" fill="none" stroke="#999" stroke-width="2"/></svg>
  <table class="compare-table">
    <colgroup><col style="width:309px"><col style="width:347px"><col style="width:349px"></colgroup>
    <tr><th>Type of Surgery</th><th>FUT (Strip Method)</th><th>FUE</th></tr>
    <tr><td>Surgery Results</td><td>Completely Natural</td><td>Completely Natural</td></tr>
    <tr><td>Shaving of Head Required</td><td>No</td><td>Yes</td></tr>
    <tr><td>Pain after the procedure</td><td>Minor</td><td>None</td></tr>
    <tr><td>Stitches required</td><td>Yes (back of head from donor area)</td><td>No</td></tr>
    <tr><td>Length of Surgery</td><td>4-6 hours</td><td>5-8 hours or longer</td></tr>
    <tr><td>Local Anesthesia</td><td>Yes</td><td>Yes</td></tr>
  </table>
</section>

<section class="section contact">
  <div class="contact-map" role="img" aria-label="Dark street map of the clinic area"></div>
  <h2 class="heading">Contact us</h2>
  <svg class="divider" style="top:134px" viewBox="0 0 240 20"><line x1="0" y1="10" x2="105" y2="10" stroke="#ccc" stroke-width="1.5"/><line x1="135" y1="10" x2="240" y2="10" stroke="#ccc" stroke-width="1.5"/><circle cx="120" cy="10" r="7" fill="none" stroke="#ddd" stroke-width="2"/></svg>
  <div class="contact-input">Enter your mail Address...</div>
  <a class="btn">Submit</a>
  <div class="contact-box">
    <div class="contact-line" style="top:42px"><svg width="14" height="14" viewBox="0 0 24 24"><path fill="#fff" d="M6.6 10.8a15 15 0 0 0 6.6 6.6l2.2-2.2a1 1 0 0 1 1-.25 11.4 11.4 0 0 0 3.6.57 1 1 0 0 1 1 1V20a1 1 0 0 1-1 1A17 17 0 0 1 3 4a1 1 0 0 1 1-1h3.5a1 1 0 0 1 1 1c0 1.25.2 2.45.57 3.6a1 1 0 0 1-.25 1z"/></svg>07700 900417</div>
    <div class="contact-line" style="top:78px;font-size:12px"><svg width="16" height="12" viewBox="0 0 16 12"><rect x="0.5" y="0.5" width="15" height="11" fill="none" stroke="#fff"/><path d="M1 1 L8 7 L15 1" fill="none" stroke="#fff"/></svg>hello@hanbithair.example</div>
    <div class="contact-brand"><span class="dot"></span>Hanbit Hair Restoration Center</div>
    <div class="social" style="left:286px;top:136px"><span></span><span></span><span></span><span></span></div>
  </div>
</section>

<section class="section testimonials">
  <h2 class="heading" style="top:56px">Testimonials</h2>
  <svg class="divider" style="top:100px" viewBox="0 0 240 20"><line x1="0" y1="10" x2="105" y2="10" stroke="#555" stroke-width="1.5"/><line x1="135" y1="10" x2="240" y2="10" stroke="#555" stroke-width="1.5"/><circle cx="120" cy="10" r="7" fill="none" stroke="#999" stroke-width="2"/></svg>

  <div class="testimonial" style="left:96px">
    <div class="testimonial-photo" role="img" aria-label="Before and after photos of a male patient"><div class="half"><span>Before</span></div><div class="half"><span>After</span></div></div>
    <h4>Mark Ellison</h4><div class="stars">★★★★★</div>
    <p>Hair on back of head is trimmed and a narrow strip is surgically removed so that hair can grow through and camouflage the scar.Hair on back of head is trimmed and a narrow strip is surgically</p>
  </div>
  <div class="testimonial" style="left:443px">
    <div class="testimonial-photo" role="img" aria-label="Before and after photos of a female patient"><div class="half" style="background:linear-gradient(180deg,#e6e1dc,#d2478e)"><span>Before</span></div><div class="half" style="background:linear-gradient(180deg,#e6e1dc,#d2478e)"><span>After</span></div></div>
    <h4>Mark Ellison</h4><div class="stars">★★★★★</div>
    <p>Hair on back of head is trimmed and a narrow strip is surgically removed so that hair can grow through and camouflage the scar.Hair on back of head is trimmed and a narrow strip is surgically</p>
  </div>
  <div class="testimonial" style="left:789px">
    <div class="testimonial-photo" role="img" aria-label="Before and after photos of a male patient in a suit"><div class="half" style="background:linear-gradient(180deg,#f2f2f2,#222)"><span>Before</span></div><div class="half" style="background:linear-gradient(180deg,#f2f2f2,#222)"><span>After</span></div></div>
    <h4>Mark Ellison</h4><div class="stars">★★★★★</div>
    <p>Hair on back of head is trimmed and a narrow strip is surgically removed so that hair can grow through and camouflage the scar.Hair on back of head is trimmed and a narrow strip is surgically</p>
  </div>
</section>

<section class="section blog">
  <h2 class="heading" style="top:42px">Latest Blog</h2>
  <svg class="divider" style="top:86px" viewBox="0 0 240 20"><line x1="0" y1="10" x2="105" y2="10" stroke="#555" stroke-width="1.5"/><line x1="135" y1="10" x2="240" y2="10" stroke="#555" stroke-width="1.5"/><circle cx="120" cy="10" r="7" fill="none" stroke="#999" stroke-width="2"/></svg>

  <article class="post" style="left:96px">
    <div class="post-img" role="img" aria-label="Man touching his thinning scalp" style="background:linear-gradient(135deg,#c98a66,#8a4f35)"></div>
    <h4>SHOULD I STAY OR SHOULD I GO?</h4>
    <div class="meta"><span>▦ Dec 23,2014</span><span>● 10 comments</span></div>
    <p>Hair on back of head is trimmed and a narrow strip is surgically removed so that hair can grow through and camouflage the scar.Hair on back of head is trimmed and a narrow strip is surgically</p>
    <a class="more">Read more &gt;&gt;</a>
  </article>
  <article class="post" style="left:443px">
    <div class="post-img" role="img" aria-label="Man checking his hairline in a mirror" style="background:linear-gradient(135deg,#e8e4df,#9d8678)"></div>
    <h4>SHOULD I STAY OR SHOULD I GO?</h4>
    <div class="meta"><span>▦ Dec 23,2014</span><span>● 10 comments</span></div>
    <p>Hair on back of head is trimmed and a narrow strip is surgically removed so that hair can grow through and camouflage the scar.Hair on back of head is trimmed and a narrow strip is surgically</p>
    <a class="more">Read more &gt;&gt;</a>
  </article>
  <article class="post" style="left:789px">
    <div class="post-img" role="img" aria-label="Top view of a thinning crown" style="background:linear-gradient(180deg,#f4f4f4,#b9a89c)"></div>
    <h4>SHOULD I STAY OR SHOULD I GO?</h4>
    <div class="meta"><span>▦ Dec 23,2014</span><span>● 10 comments</span></div>
    <p>Hair on back of head is trimmed and a narrow strip is surgically removed so that hair can grow through and camouflage the scar.Hair on back of head is trimmed and a narrow strip is surgically</p>
    <a class="more">Read more &gt;&gt;</a>
  </article>
</section>

<footer class="section site-footer">
  <p class="copy">Copyright 2016 Hanbit Hair Center. All Rights Reserved</p>
  <div class="footer-icons"><span></span><span></span><span></span><span></span><span></span><span></span></div>
</footer>

</body>
</html>
```